Church Lanterns Over Millbrook Gospel Booklet Design

We need a booklet designed that we will be printing to hand out in our community. Wording for each page will be provided and we need graphic design to produce the layouts in a format ready for print. Booklet will be 4.75" x 4.75" square and a total of 12 pages: 1 cover page front, 1 cover page back, 10 inside pages some of which will be full spread across 2 pages.

Target Market(s)

English speaking Westerners

Industry/Entity Type

Religious

Font styles to use
Serif

Colors
ffffff
85abd2
0292cd
33b8a4
5c5c5c

Requirements
Must have
• Minimalist design with clean look described in attached document
Nice to have
• Aesthetically pleasing graphics, crisp fonts, excellent turn around times
Should not have
• Effeminate design, busy look with too much graphic and text

```html
<!DOCTYPE html>
<html lang="en">
<head>
<meta charset="utf-8">
<title>Lanterns Over Millbrook – Salvation Spread</title>
<link rel="stylesheet" href="https://fonts.googleapis.com/css2?family=Nunito:wght@800&family=Lora:wght@400&display=swap">
<style>
  :root {
    --white: #ffffff;
    --sky-blue: #85abd2;
    --heading-blue: #84a8d0;
    --mist-light: #e4e4e2;
    --mist-mid: #b9bdb5;
    --hill-green: #6f7b5a;
    --hill-dark: #4f5a45;
  }
  * { box-sizing: border-box; margin: 0; padding: 0; }
  html, body {
    width: 1200px;
    height: 600px;
    overflow: hidden;
    background: var(--white);
  }
  .spread {
    position: relative;
    width: 1200px;
    height: 600px;
    background: var(--white);
  }
  .photo {
    position: absolute;
    background: linear-gradient(180deg, var(--mist-light) 0%, var(--mist-mid) 40%, var(--hill-green) 78%, var(--hill-dark) 100%);
  }
  .photo--left-hero { left: 0; top: 0; width: 603px; height: 303px; }
  .photo--top-strip {
    left: 603px; top: 0; width: 597px; height: 82px;
    background: linear-gradient(180deg, var(--mist-light) 0%, var(--mist-mid) 100%);
  }
  .photo--right-panel { left: 929px; top: 95px; width: 271px; height: 497px; }

  .salvation-steps {
    position: absolute;
    left: 58px;
    top: 336px;
    width: 490px;
    text-align: center;
    color: var(--heading-blue);
    font-family: "Nunito", sans-serif;
    font-weight: 800;
    font-size: 17px;
    line-height: 25px;
  }
  .salvation-steps__title { margin-bottom: 25px; }

  .verse-panel {
    position: absolute;
    left: 617px;
    top: 95px;
    width: 299px;
    height: 505px;
    background: var(--sky-blue);
  }
  .verse-panel__quote {
    position: absolute;
    left: 30px;
    right: 30px;
    top: 144px;
    text-align: center;
    color: var(--white);
    font-family: "Lora", serif;
    font-size: 18.5px;
    line-height: 28px;
  }
</style>
</head>
<body>
  <main class="spread">
    <div class="photo photo--left-hero" role="img" aria-label="Woman with raised arms on a misty green mountainside"></div>
    <div class="photo photo--top-strip" role="img" aria-label="Raised hands against a misty sky"></div>

    <section class="salvation-steps">
      <p class="salvation-steps__title">Here is what you must do to be saved:</p>
      <p class="salvation-steps__body">First, ask Jesus Christ to save you (Since he is God, he can hear you): Acknowledge that God is the rightful authority of the universe and your life. Apologize to him for your rebellion against God. Ask Jesus Christ to come into your life as your Lord and Savior. This decision will immediately trigger his miracle of salvation in you. God now lives in you!</p>
    </section>

    <aside class="verse-panel">
      <blockquote class="verse-panel__quote">“If you confess with your mouth that Jesus is Lord and believe in your heart that God raised him from the dead, you will be saved.” (Romans 10:9)</blockquote>
    </aside>

    <div class="photo photo--right-panel" role="img" aria-label="Woman in a blue jacket raising her arms toward misty hills"></div>
  </main>
</body>
</html>
```